Digital course framework design and style

We need a design for a framework to be used on an online course. The framework will have several layers and needs to have a style which can be followed throughout the course. The attached image is at the top level.

Need to keep to the triangle shape and the colour green and red for the words shown in the illustration. The three inner sections are pillars/pathways which we will expand out (Health, Adventure, Creativity) .
The course is Puddles to Pinecones (the inner section) so we need to show the flow from being frustrated with your kids on devices and not trying to be a successful and they can be, moving them to there kids taking action and frustration reducing. So important the framework has the feeling of progression and movement. The issue for each pillar/paths is the red text and the green being the result.

I want the framework to be simple to understand keeping to line diagram but introducing an icon for each piller/path. Needs to look professional and engaging.

I need to be able to edit the framework, present it elements so be in a format I can hide each Piller and display on a mouse click so layered.

Colours should fit into the brand colours

Core colour: #f07f37
Black secondary: #070707
Green : #0A633B
White: #FFFEFE

Website for brand approach: www.meadowandlantern.com

Target Market(s)

Parents of children spending too long on devices

Font styles to use
Sans Serif

Requirements
Must have
• Clear and easy to see outcomes (green words on the example)
Flow from problem to solution (Puddles to Pinecones)
Style to be extended to further piller designs including icons for Health, Adventure, Creativity
Ability to present 1) the promise Puddles to Pinecones 2) each piller in turn
Brand colours included in brief
Should not have
• Busy complicated slide
Keep to line art not complex images

```html
<!DOCTYPE html>
<html lang="en">
<head>
<meta charset="utf-8">
<title>Puddles to Pinecones – Course Framework</title>
<link href="https://fonts.googleapis.com/css2?family=Nunito:wght@400;800;900&family=Questrial&display=swap" rel="stylesheet">
<style>
  :root {
    --orange: #f07f37;
    --green: #0a633b;
    --red: #e8141b;
    --grey: #6d6e71;
    --grey-text: #ececec;
    --white: #fffefe;
    --black: #070707;
  }
  html, body {
    margin: 0;
    padding: 0;
    width: 1200px;
    height: 1000px;
    overflow: hidden;
    background: var(--white);
  }
  .framework {
    display: block;
    width: 1200px;
    height: 1000px;
  }
  .outer-ring { fill: none; stroke: var(--green); stroke-width: 3; }
  .problem-band { fill: var(--grey); }
  .pillar-band { fill: var(--orange); }
  .core { fill: var(--white); }
  .divider { stroke: var(--white); stroke-width: 5; stroke-linecap: round; }

  .outcome {
    font-family: "Nunito", sans-serif;
    font-weight: 900;
    font-size: 40px;
    fill: var(--green);
    text-anchor: middle;
  }
  .problem {
    font-family: "Questrial", sans-serif;
    font-size: 20px;
    fill: var(--grey-text);
    text-anchor: middle;
  }
  .pillar-name {
    font-family: "Nunito", sans-serif;
    font-weight: 900;
    font-size: 36px;
    fill: var(--white);
    text-anchor: middle;
    letter-spacing: 0.5px;
  }
  .promise-result {
    font-family: "Nunito", sans-serif;
    font-weight: 900;
    font-size: 40px;
    fill: var(--green);
    text-anchor: middle;
  }
  .promise-start {
    font-family: "Nunito", sans-serif;
    font-weight: 900;
    font-size: 36px;
    fill: var(--red);
    text-anchor: middle;
  }
  .flow-arrow { fill: none; stroke: url(#flowGradient); stroke-width: 3; stroke-linejoin: miter; }
  .icon { fill: none; stroke: var(--white); stroke-width: 3; stroke-linecap: round; stroke-linejoin: round; }
  .icon-fill { fill: var(--white); }
  .brand-name {
    font-family: "Nunito", sans-serif;
    font-weight: 400;
    font-size: 30px;
    fill: var(--orange);
    text-anchor: middle;
  }
</style>
</head>
<body>
<svg class="framework" viewBox="0 0 1200 1000" xmlns="http://www.w3.org/2000/svg" aria-label="Puddles to Pinecones course framework">
  <defs>
    <linearGradient id="flowGradient" x1="0" y1="1" x2="0" y2="0">
      <stop offset="0" stop-color="#e8141b"/>
      <stop offset="1" stop-color="#0a633b"/>
    </linearGradient>
  </defs>

  <circle class="outer-ring" cx="600" cy="500" r="447"/>

  <!-- Triangle layers -->
  <g class="triangle">
    <polygon class="problem-band" points="600,55 205,735 995,735"/>
    <polygon class="pillar-band" points="600,208 340,656 860,656"/>
    <polygon class="core" points="600,310 430,605 770,605"/>
    <line class="divider" x1="600" y1="55" x2="600" y2="310"/>
    <line class="divider" x1="205" y1="735" x2="430" y2="605"/>
    <line class="divider" x1="995" y1="735" x2="770" y2="605"/>
  </g>

  <!-- Health pillar -->
  <g class="pillar pillar-health">
    <text class="outcome" transform="translate(318,335) rotate(-59.8)">
      <tspan x="0" y="-24">Balanced, Fit,</tspan>
      <tspan x="0" y="26">Energetic &amp; Focused</tspan>
    </text>
    <text class="problem" transform="translate(430,412) rotate(-59.8)" y="7">Anxious, Overweight, Unfit &amp; Disconnected</text>
    <text class="pillar-name" transform="translate(508,440) rotate(-59.8)" y="13">HEALTH</text>
    <g class="icon-heart" transform="translate(445,548) rotate(-59.8)">
      <path class="icon-fill" d="M0,10 C-14,0 -20,-8 -16,-16 C-12,-23 -3,-22 0,-15 C3,-22 12,-23 16,-16 C20,-8 14,0 0,10 Z"/>
      <polyline class="icon" points="-46,0 -34,0 -29,-10 -24,10 -19,0 -16,0"/>
    </g>
  </g>

  <!-- Creativity pillar -->
  <g class="pillar pillar-creativity">
    <text class="outcome" transform="translate(872,345) rotate(59.8)">
      <tspan x="0" y="-24">Bright, Idea Driven,</tspan>
      <tspan x="0" y="26">Positive &amp; Motivated</tspan>
    </text>
    <text class="problem" transform="translate(770,412) rotate(59.8)" y="7">Unimaginative, negative, screen focused &amp; trapped</text>
    <text class="pillar-name" transform="translate(728,488) rotate(59.8)" y="13">CREATIVITY</text>
    <g class="icon-palette" transform="translate(642,335) rotate(59.8)">
      <path class="icon" d="M0,-16 C-14,-16 -22,-6 -20,4 C-18,14 -6,18 4,16 C10,15 8,8 12,6 C17,4 22,2 20,-4 C17,-12 9,-16 0,-16 Z"/>
      <circle class="icon-fill" cx="-10" cy="-4" r="2.5"/>
      <circle class="icon-fill" cx="-3" cy="-9" r="2.5"/>
      <circle class="icon-fill" cx="-9" cy="7" r="2.5"/>
      <line class="icon" x1="4" y1="4" x2="22" y2="-22"/>
    </g>
  </g>

  <!-- Adventure pillar -->
  <g class="pillar pillar-adventure">
    <text class="outcome" x="592" y="812">Curious, Connected,</text>
    <text class="outcome" x="592" y="862">Excited &amp; Leading</text>
    <text class="problem" x="600" y="709">Inactive, Insular, Solitary &amp; Timid</text>
    <text class="pillar-name" x="558" y="645" style="font-size:34px">ADVENTURE</text>
    <g class="icon-mountains" transform="translate(715,632)">
      <polyline class="icon" points="-20,14 -6,-6 2,4 12,-14 28,14"/>
      <polyline class="icon" points="8,-8 12,-4 16,-8"/>
      <path class="icon-fill" d="M-30,-6 a5,5 0 0 1 6,-7 a6,6 0 0 1 11,1 a4,4 0 0 1 2,8 z"/>
    </g>
  </g>

  <!-- Promise: Puddles to Pinecones -->
  <g class="promise">
    <text class="promise-result" x="600" y="470">ACTION</text>
    <polygon class="flow-arrow" points="600,484 624,508 612,508 612,540 588,540 588,508 576,508"/>
    <text class="promise-start" x="600" y="586">FRUSTRATION</text>
  </g>

  <!-- Brand -->
  <g class="brand">
    <text class="brand-name" x="1076" y="878">Meadow</text>
    <text class="brand-name" x="1076" y="914">&amp; Lantern</text>
  </g>
</svg>
</body>
</html>
```